I need Business Cards and Letterhead Designed

I have a current label so I just need the template design. It should be clean and should look rich. I own a Wealth Management/Investment Advisory business and I need to brand to look substantial & mature.

The Business Cards may be one or two sided and may be a standard or non-standard size. I will likely print on very thick stock but not a requirement. Embossment or foil are also something that I may consider but is not required.
Updates

Getting some great designs, thank you all for your hard work. I have returned from a trip and will be posting individual feedback over the next day or so. In the meantime please note the following:

1st. My disclosure should be posted at the bottom or back of the card. It may be in smaller print but it must be listed as follows "all together";

Securities offered through Pelgrave Brokerage, Inc. A Registered Broker/Dealer. Member NOBKA/DEXO. Gil Prawley, Registered Representative. Advisory Services offered through Halden Brightwell an RBO Registered Investment Advisory Firm. RJV Wealth Management, Pelgrave Brokerage and Halden Brightwell are unaffiliated. CA Insurance Lic.# 0K42573

2nd. My Title should be listed as President / CEO
&
I need the following contact information included:

Address:
418 Verlow Blvd
Suite 740
Costa Mesa, CA  92626

Phone; 949-555-0173
fax: 800-555-0148
email: gil.prawley@pelgravebrokerage.com

Thank you for your help.

Best regards,

GP

Target Market(s)

Affluent Individuals & Families. C-Level Executives, Women, Accountants, Attorneys, Business Owners

Industry/Entity Type

Business

Requirements
Must have
• Both my cards and letterhead must include the following disclosure:

Securities offered through Pelgrave Brokerage, Inc. A Registered Broker/Dealer. Member NOBKA/DEXO.
Gil Prawley, Registered Representative. Advisory Services offered through Halden Brightwell an RBO Registered Investment Advisory Firm. RJV Wealth Management, Pelgrave Brokerage and Halden Brightwell are unaffiliated. CA Insurance Lic.# 0K4257
Should not have
• Do not include illustrations of money bags or gold bullion, or "$" signs or anything of that type.

```html
<!DOCTYPE html>
<html lang="en">
<head>
<meta charset="utf-8">
<title>RJV Wealth Management – Stationery</title>
<link rel="stylesheet" href="https://fonts.googleapis.com/css2?family=Crimson+Pro:wght@400;600&display=swap">
<style>
  :root {
    --backdrop: #5a5a5c;
    --brown: #521a00;
    --cream: #f5eedf;
    --tan: #b98d6f;
    --tan-dark: #9a5a38;
    --ink: #5a1f05;
    --accent: #a8684a;
    --muted: #8b6a58;
    --serif: "Crimson Pro", Georgia, serif;
  }
  * { box-sizing: border-box; margin: 0; padding: 0; }
  html, body { width: 1200px; height: 1000px; overflow: hidden; }
  body { background: var(--backdrop); font-family: var(--serif); color: var(--ink); position: relative; }

  .piece { position: absolute; }
  .sheet { background: var(--cream); }
  .dark { background: var(--brown); }

  .stripe {
    position: absolute; left: 0; right: 0; bottom: 0;
    background: repeating-linear-gradient(90deg, var(--tan) 0 15%, var(--tan-dark) 15% 30%);
  }
  .tab { position: absolute; top: 0; background: var(--tan); }

  .brand { display: flex; align-items: center; gap: 0.35em; white-space: nowrap; }
  .brand-square { width: 0.9em; height: 0.9em; background: var(--ink); flex: none; }
  .brand-name { font-weight: 600; color: var(--ink); letter-spacing: 0.02em; }

  .label {
    position: absolute; background: var(--cream);
    display: flex; align-items: center; justify-content: center;
  }

  /* Folder */
  .folder { left: 56px; top: 164px; width: 362px; height: 492px; }
  .folder .tab { left: 120px; width: 122px; height: 16px; }
  .folder .label { left: 120px; top: 16px; width: 122px; height: 68px; font-size: 8.6px; }
  .folder .stripe { height: 18px; }

  /* Letterhead */
  .letterhead { left: 342px; top: 122px; width: 346px; height: 488px; }
  .letterhead .tab { left: 32px; width: 98px; height: 15px; }
  .letterhead .brand { position: absolute; left: 34px; top: 28px; font-size: 10.5px; }
  .letter-heading { position: absolute; left: 34px; top: 154px; width: 200px; font-size: 11.5px; line-height: 14px; color: var(--accent); font-weight: 400; }
  .letter-body { position: absolute; left: 34px; top: 194px; width: 286px; font-size: 6.1px; line-height: 7.6px; color: var(--ink); }
  .letter-body p + p { margin-top: 5px; }
  .letter-sign { position: absolute; left: 34px; top: 373px; font-size: 6.4px; }
  .letter-contact { position: absolute; left: 30px; top: 445px; font-size: 5.6px; line-height: 7.4px; color: var(--muted); }
  .letter-contact b { font-weight: 400; color: var(--ink); }
  .letterhead .stripe { height: 8px; }

  /* Small cards */
  .mini-back { left: 856px; top: 75px; width: 149px; height: 80px; }
  .mini-back .label { left: 42px; top: 16px; width: 62px; height: 26px; font-size: 4.3px; }
  .mini-back .tab { left: 42px; width: 62px; height: 6px; }
  .mini-back .stripe { height: 7px; }

  .mini-front { left: 966px; top: 131px; width: 150px; height: 80px; }
  .mini-front .tab { left: 45px; width: 60px; height: 5px; }
  .mini-front .brand { position: absolute; left: 52px; top: 10px; font-size: 5.5px; }
  .mini-name { position: absolute; left: 0; right: 0; top: 29px; text-align: center; font-size: 7px; }
  .mini-title { position: absolute; left: 0; right: 0; top: 38px; text-align: center; font-size: 3.6px; color: var(--muted); }
  .mini-contact { position: absolute; left: 0; right: 0; top: 47px; text-align: center; font-size: 3.4px; line-height: 4.6px; color: var(--ink); }
  .mini-legal { position: absolute; left: 6px; right: 6px; top: 63px; font-size: 2.2px; line-height: 2.8px; color: var(--muted); text-align: center; }
  .mini-front .stripe { height: 6px; }

  /* Envelope back */
  .envelope-back { left: 719px; top: 262px; width: 362px; height: 230px; }

  /* Envelope front */
  .envelope { left: 794px; top: 397px; width: 362px; height: 183px; }
  .envelope .tab { left: 24px; width: 76px; height: 12px; }
  .envelope .brand { position: absolute; left: 26px; top: 24px; font-size: 8.5px; }
  .envelope-contact { position: absolute; left: 24px; top: 130px; font-size: 5.6px; line-height: 7.2px; color: var(--ink); }
  .envelope-contact span { color: var(--muted); }
  .envelope .stripe { height: 15px; }

  /* Business card front */
  .card { left: 295px; top: 744px; width: 344px; height: 181px; }
  .card .tab { left: 101px; width: 141px; height: 12px; }
  .card .brand { position: absolute; left: 0; right: 0; top: 28px; justify-content: center; font-size: 13px; }
  .card-name { position: absolute; left: 0; right: 0; top: 82px; text-align: center; font-size: 14.5px; }
  .card-title { position: absolute; left: 112px; right: 112px; top: 99px; padding-bottom: 2px; border-bottom: 0.6px solid var(--tan); text-align: center; font-size: 7.5px; color: var(--accent); }
  .card-contact { position: absolute; left: 0; right: 0; top: 119px; text-align: center; font-size: 7.8px; line-height: 11px; color: var(--ink); }
  .card-contact span { color: var(--accent); }
  .card-legal { position: absolute; left: 8px; right: 8px; top: 154px; text-align: center; font-size: 3.6px; line-height: 4.4px; color: var(--muted); }
  .card .stripe { height: 12px; }

  /* Business card back */
  .card-back { left: 660px; top: 740px; width: 344px; height: 181px; }
  .card-back .tab { left: 110px; width: 142px; height: 14px; }
  .card-back .label { left: 110px; top: 14px; width: 142px; height: 112px; font-size: 10px; }
  .card-back .stripe { height: 12px; }
</style>
</head>
<body>

  <section class="piece folder dark" aria-label="Presentation folder">
    <div class="tab"></div>
    <div class="label"><div class="brand"><span class="brand-square"></span><span class="brand-name">RJV Wealth Management</span></div></div>
    <div class="stripe"></div>
  </section>

  <section class="piece letterhead sheet" aria-label="Letterhead">
    <div class="tab"></div>
    <div class="brand"><span class="brand-square"></span><span class="brand-name">RJV Wealth Management</span></div>
    <h1 class="letter-heading">Lorem ipsum dolor sit amet, consectetur adipiscing elit. Etiam a diam lorem.</h1>
    <div class="letter-body">
      <p>Lorem ipsum dolor sit amet, consectetur adipiscing elit. Etiam a diam lorem. Proin lectus tellus, tincidunt sit amet est tristique, facilisis ultricies nibh. In tristique, tortor feugiat tempor porttitor, eros erat sagittis leo, non pellentesque ante ante in velit. Vestibulum vitae velit a odio facilisis pulvinar non porta elit. Fusce a malesuada nunc. Nullam sit amet ante vitae lectus pretium tristique a et mauris. Proin id lacus lorem. Etiam porta porttitor mauris, ac posuere elit fermentum eu. Praesent non cursus magna. Integer blandit arcu eu, non egestas mauris lobortis at. Aliquam in magna ac dolor sodales pharetra.</p>
      <p>Ut euismod eleifend tellus, vel tempus nulla aliquet at. Quisque tellus magna, sollicitudin sed libero eget, mollis aliquet est. Nulla ut lectus velit. Integer neque libero, ornare eget augue nec, bibendum mattis mauris. Suspendisse potenti. Sed blandit a mauris a rutrum. Integer mattis non augue non tempor. Mauris ut lacus sem. Phasellus eros urna, imperdiet sit amet magna ut, tincidunt blandit erat. Etiam massa est, imperdiet nec iaculis quis, porta at felis.</p>
      <p>Proin convallis placerat porta. Donec semper convallis urna in viverra. Sed at mauris luctus, cursus eros et, auctor metus. Aliquam adipiscing aliquet urna, ut mollis risus pharetra ut. Nunc vulputate facilisis euismod. Curabitur laoreet ante euismod nulla eleifend, in pulvinar libero interdum. Suspendisse malesuada molestie dignissim.</p>
    </div>
    <p class="letter-sign">Gilbert Prawley</p>
    <div class="letter-contact">
      <p>Address: <b>418 Verlow Blvd., Suite 740 • Harlow Bay, CA 92718</b></p>
      <p>Phone: <b>949.555.0173</b> &nbsp; Fax: <b>800.555.0148</b> &nbsp; Email: <b>gil.prawley@pelgravebrokerage.com</b></p>
    </div>
    <div class="stripe"></div>
  </section>

  <section class="piece mini-back dark" aria-label="Business card back, small">
    <div class="tab"></div>
    <div class="label"><div class="brand"><span class="brand-square"></span><span class="brand-name">RJV Wealth Management</span></div></div>
    <div class="stripe"></div>
  </section>

  <section class="piece mini-front sheet" aria-label="Business card front, small">
    <div class="tab"></div>
    <div class="brand"><span class="brand-square"></span><span class="brand-name">RJV Wealth</span></div>
    <p class="mini-name">Gilbert Prawley</p>
    <p class="mini-title">President / CEO</p>
    <div class="mini-contact">
      <p>Address: 418 Verlow Blvd., Suite 740 • Harlow Bay, CA 92718</p>
      <p>Phone: 949.555.0173 &nbsp; Fax: 800.555.0148 &nbsp; Email: gil.prawley@pelgravebrokerage.com</p>
    </div>
    <p class="mini-legal">Securities offered through Pelgrave Brokerage, Inc. A Registered Broker/Dealer. Member NOBKA/DEXO. Gil Prawley, Registered Representative. Advisory Services offered through Halden Brightwell an RBO Registered Investment Advisory Firm. RJV Wealth Management, Pelgrave Brokerage and Halden Brightwell are unaffiliated. CA Insurance Lic.# 0K42573</p>
    <div class="stripe"></div>
  </section>

  <svg class="piece envelope-back" viewBox="0 0 362 230" aria-label="Envelope back">
    <rect x="0" y="44" width="362" height="186" fill="var(--cream)"/>
    <path d="M0 46 L20 0 L342 0 Q350 0 354 8 L362 46 L181 132 Z" fill="var(--brown)"/>
  </svg>

  <section class="piece envelope sheet" aria-label="Envelope front">
    <div class="tab"></div>
    <div class="brand"><span class="brand-square"></span><span class="brand-name">RJV Wealth</span></div>
    <div class="envelope-contact">
      <p><span>Address:</span> 418 Verlow Blvd., Suite 740</p>
      <p>Harlow Bay, CA 92718</p>
      <p><span>Phone:</span> 949.555.0173 &nbsp; <span>Fax:</span> 800.555.0148</p>
      <p><span>Email:</span> gil.prawley@pelgravebrokerage.com</p>
    </div>
    <div class="stripe"></div>
  </section>

  <section class="piece card sheet" aria-label="Business card front">
    <div class="tab"></div>
    <div class="brand"><span class="brand-square"></span><span class="brand-name">RJV Wealth Management</span></div>
    <p class="card-name">Gilbert Prawley</p>
    <p class="card-title">President / CEO</p>
    <div class="card-contact">
      <p><span>Address:</span> 418 Verlow Blvd., Suite 740 • Harlow Bay, CA 92718</p>
      <p><span>Phone:</span> 949.555.0173 &nbsp; <span>Fax:</span> 800.555.0148 &nbsp; <span>Email:</span> gil.prawley@pelgravebrokerage.com</p>
    </div>
    <p class="card-legal">Securities offered through Pelgrave Brokerage, Inc. A Registered Broker/Dealer. Member NOBKA/DEXO. Gil Prawley, Registered Representative. Advisory Services offered through Halden Brightwell an RBO Registered Investment Advisory Firm. RJV Wealth Management, Pelgrave Brokerage and Halden Brightwell are unaffiliated. CA Insurance Lic.# 0K42573</p>
    <div class="stripe"></div>
  </section>

  <section class="piece card-back dark" aria-label="Business card back">
    <div class="tab"></div>
    <div class="label"><div class="brand"><span class="brand-square"></span><span class="brand-name">RJV Wealth Management</span></div></div>
    <div class="stripe"></div>
  </section>

</body>
</html>
```